Bref créative
Business card/letterhead/envelopes/fax cover sheet for plastic surgery practice
Morvan Plastic Surgery
Professional
Darek Olund, M.D.
unknown at this time
morvanaestheticclinic@mailbeam.example
www.darekolundmd.example
I would like name, address, phone number, fax number, and website included on front (no email address). I would also like the Continental Guild of Cosmetic Practice logo and Board Certified logo to appear on the front. The words "Plastic and Reconstructive Surgery, Hand Surgery, Cosmetic Surgery" should appear near or under my name.
The tagline "Results nobody can resist" should be included (front or back). Also, an area to write in the next appointment information should be on the back.
Continental Guild of Cosmetic Practitioners Logo
logo
Board Certification logo

```html
<!DOCTYPE html>
<html lang="en">
<head>
<meta charset="utf-8">
<title>Morvan Plastic Surgery – Business Card</title>
<link href="https://fonts.googleapis.com/css2?family=PT+Serif:ital,wght@0,400;0,700;1,400&display=swap" rel="stylesheet">
<style>
  :root{
    --bg:#e6e7ea;
    --card:#ffffff;
    --navy:#1f3773;
    --blue:#2c5fb3;
    --ink:#4a4d55;
    --muted:#8a8d94;
    --rule:#b9bcc3;
    --accent-gold:#e0a526;
    --accent-teal:#3aa7c9;
  }
  *{box-sizing:border-box;margin:0;padding:0}
  html,body{width:1200px;height:901px;overflow:hidden}
  body{background:var(--bg);font-family:"PT Serif",Georgia,serif;color:var(--ink);position:relative}
  .card{position:absolute;left:250px;width:700px;height:400px;background:var(--card);
    border-radius:22px;box-shadow:0 8px 24px rgba(0,0,0,.18);overflow:hidden}
  .card-back{top:40px}
  .card-front{top:465px}

  /* back */
  .appt-title{position:absolute;top:62px;width:100%;text-align:center;color:var(--navy);font-size:30px;font-weight:700}
  .appt-row{position:absolute;left:60px;right:60px;display:flex;align-items:flex-end;gap:12px;color:var(--navy);font-size:24px}
  .appt-row .line{flex:1;border-bottom:1.5px solid var(--rule);height:24px}
  .row-for{top:130px}.row-date{top:188px}.row-time{top:246px}
  .appt-web{position:absolute;top:300px;width:100%;text-align:center;letter-spacing:7px;color:var(--ink);font-size:16px}
  .appt-note{position:absolute;top:345px;width:100%;text-align:center;font-size:13px;color:var(--ink)}

  /* front */
  .edge-tab{position:absolute;top:0;right:0;width:34px;height:46px;background:linear-gradient(90deg,#c7c9ce,#8c8f96)}
  .edge-bar{position:absolute;left:0;top:215px;width:10px;height:140px;background:linear-gradient(180deg,var(--blue),var(--navy))}
  .brand{position:absolute;left:46px;top:46px;color:var(--navy);font-weight:700}
  .brand .name{font-size:44px;letter-spacing:4px;line-height:1}
  .brand .sub{font-size:15px;letter-spacing:5px;margin-top:4px}
  .address{position:absolute;left:46px;top:152px;font-size:17px;line-height:1.3;color:var(--ink)}
  .contacts{position:absolute;left:46px;top:210px;list-style:none;font-size:17px;line-height:1}
  .contacts li{display:flex;align-items:center;gap:10px;height:24px}
  .contacts .ico{width:18px;height:18px;flex:none}
  .contacts .main{color:var(--navy);font-weight:700;font-size:20px}
  .tagline{position:absolute;left:46px;top:340px;font-size:23px;color:var(--ink)}
  .tagline b{color:var(--blue)}
  .doctor{position:absolute;right:58px;top:40px;text-align:right}
  .doctor .dr{color:var(--navy);font-weight:700;font-size:23px}
  .doctor .spec{font-size:14px;line-height:1.35;color:var(--ink);margin-top:4px}
  .member{position:absolute;left:470px;top:200px;font-size:12px;color:var(--ink)}
  .badges{position:absolute;left:460px;top:218px;display:flex;gap:34px;align-items:center}
</style>
</head>
<body>

<section class="card card-back" aria-label="Card back">
  <h2 class="appt-title">Next Appointment</h2>
  <div class="appt-row row-for"><span>For :</span><span class="line"></span></div>
  <div class="appt-row row-date"><span>Date :</span><span class="line"></span></div>
  <div class="appt-row row-time"><span>Time :</span><span class="line"></span></div>
  <p class="appt-web">www.darekolundmd.example</p>
  <p class="appt-note">If you are unable to keep your appointment please call the office 24 hours in advance.</p>
</section>

<section class="card card-front" aria-label="Card front">
  <div class="edge-tab"></div>
  <div class="edge-bar"></div>

  <div class="brand">
    <div class="name">MORVAN</div>
    <div class="sub">PLASTIC SURGERY</div>
  </div>

  <p class="address">Suite 102 Street name,<br>State, Zip 2034, Country</p>

  <ul class="contacts">
    <li>
      <svg class="ico" viewBox="0 0 20 20"><circle cx="10" cy="10" r="10" fill="var(--navy)"/><path d="M6 5c1 0 1.5 2 1.5 2.5S6.5 8.5 7 9.5s2 2.5 3 3 1.5-.5 2-.5 2.5.5 2.5 1.5-1 1.5-2 1.5C8 15 5 12 5 7c0-1 .5-2 1-2z" fill="#fff"/></svg>
      <span class="main">212 555 0147</span>
    </li>
    <li>
      <svg class="ico" viewBox="0 0 20 20"><circle cx="10" cy="10" r="10" fill="var(--navy)"/><rect x="5" y="8" width="10" height="6" fill="#fff"/><rect x="7" y="5" width="6" height="3" fill="#fff"/></svg>
      <span>212 555 0148</span>
    </li>
    <li>
      <svg class="ico" viewBox="0 0 20 20"><circle cx="10" cy="10" r="10" fill="var(--navy)"/><rect x="5" y="6.5" width="10" height="7" fill="#fff"/><path d="M5 6.5l5 4 5-4" stroke="var(--navy)" fill="none"/></svg>
      <span>morvanaestheticclinic@mailbeam.example</span>
    </li>
    <li>
      <svg class="ico" viewBox="0 0 20 20"><circle cx="10" cy="10" r="10" fill="var(--navy)"/><circle cx="10" cy="10" r="5" fill="none" stroke="#fff"/><path d="M5 10h10M10 5c-2.5 3-2.5 7 0 10M10 5c2.5 3 2.5 7 0 10" stroke="#fff" fill="none"/></svg>
      <span>www.darekolundmd.example</span>
    </li>
  </ul>

  <p class="tagline">Results no<b>body</b> can resist</p>

  <div class="doctor">
    <div class="dr">Darek Olund, M.D.</div>
    <div class="spec">Plastic &amp; Reconstructive Surgery,<br>Hand Surgery, Cosmetic Surgery</div>
  </div>

  <p class="member">Member</p>
  <div class="badges">
    <svg width="70" height="70" viewBox="0 0 70 70" role="img" aria-label="Continental Guild of Cosmetic Practice membership badge"><circle cx="35" cy="35" r="30" fill="none" stroke="var(--accent-teal)" stroke-width="4"/></svg>
    <svg width="70" height="70" viewBox="0 0 70 70" role="img" aria-label="Board certification badge"><circle cx="35" cy="35" r="22" fill="var(--accent-gold)"/></svg>
  </div>
</section>

</body>
</html>
```